Lumora Pathway Advisory - Business card design needed

I wish to get business cards designed so that it follows my website design ... http://www.lumora-pathway.org
I need logos for QUVEX 7 and KT Summit Associate for myself which I have uploaded the files.
I wish my qualifications PhD PMP FAICD to be smaller print than my name.
Regards
Leopold
Industry/Entity Type
Business
Contact Information for Business Card
Lumora Pathway Advisory
Dr Leopold Marsh PhD PMP FAICD
Director
PO Box 418 Kelvendale NSW 2093 AUSTRALIA
T:+61 2 9352 6710 M:+61 437 918000 F: +61 2 9368 2000
Email: leopold.marsh@lumora-pathway.org
Website: http://www.lumora-pathway.org

```html
<!DOCTYPE html>
<html lang="en">
<head>
<meta charset="utf-8">
<title>Dr Leopold Marsh – Business Card</title>
<link href="https://fonts.googleapis.com/css2?family=Oswald:wght@400;500&display=swap" rel="stylesheet">
<style>
  :root {
    --backdrop: #1e1e1e;
    --card-top: #5ff0e6;
    --card-mid: #8af5ec;
    --card-low: #4fe6dc;
    --brand-green: #1f7d1c;
    --deep-green: #146a14;
    --ink: #1a1a1a;
    --muted: #2b2b2b;
    --swoosh: #0a0a0a;
    --swoosh-light: #d9d9d9;
    --badge: #4cc9f0;
  }
  html, body {
    margin: 0;
    width: 1200px;
    height: 900px;
    overflow: hidden;
    background: var(--backdrop);
    font-family: "Oswald", "Arial Narrow", sans-serif;
  }
  .card {
    position: absolute;
    left: 158px;
    top: 65px;
    width: 975px;
    height: 685px;
    border-radius: 10px;
    overflow: hidden;
    background: linear-gradient(180deg, var(--card-top) 0%, var(--card-mid) 45%, var(--card-low) 100%);
  }
  .card-swoosh {
    position: absolute;
    left: 0;
    top: 0;
    width: 975px;
    height: 685px;
  }
  .certification-mark {
    position: absolute;
    left: 32px;
    top: 60px;
    width: 100px;
    height: 100px;
    border-radius: 50%;
    background: var(--brand-green);
  }
  .certification-name {
    position: absolute;
    left: 157px;
    top: 68px;
    width: 293px;
    font-size: 28px;
    font-weight: 400;
    line-height: 1.2;
    color: var(--deep-green);
    white-space: nowrap;
  }
  .certification-rule {
    position: absolute;
    left: 157px;
    top: 127px;
    width: 293px;
    height: 2px;
    background: var(--deep-green);
  }
  .certification-level {
    position: absolute;
    left: 157px;
    top: 137px;
    font-size: 22px;
    font-weight: 500;
    line-height: 1.2;
    color: var(--deep-green);
    letter-spacing: 1px;
  }
  .holder {
    position: absolute;
    right: 35px;
    top: 155px;
    text-align: right;
  }
  .holder-name {
    margin: 0;
    font-size: 66px;
    font-weight: 500;
    line-height: 1;
    color: var(--brand-green);
  }
  .holder-rule {
    margin: 8px 0 0 auto;
    width: 430px;
    height: 2px;
    background: linear-gradient(90deg, transparent, #7a8a8a 20%, #7a8a8a);
  }
  .holder-credentials {
    margin-top: 14px;
    font-size: 21px;
    color: var(--muted);
    letter-spacing: 0.5px;
  }
  .contact-list {
    position: absolute;
    left: 312px;
    top: 294px;
    margin: 0;
    padding: 0;
    list-style: none;
  }
  .contact-item {
    display: flex;
    align-items: center;
    height: 62px;
    font-size: 37px;
    color: var(--brand-green);
    white-space: nowrap;
  }
  .contact-icon {
    width: 40px;
    height: 40px;
    margin-right: 22px;
    flex: none;
  }
  .contact-item.is-continued {
    padding-left: 62px;
  }
  .partner-badge {
    position: absolute;
    left: 747px;
    top: 556px;
    width: 220px;
    height: 86px;
    border-radius: 4px;
    background: var(--badge);
  }
</style>
</head>
<body>
  <main class="card">
    <svg class="card-swoosh" viewBox="0 0 975 685" aria-hidden="true">
      <path d="M0,548 C70,625 230,640 420,612 C300,650 200,662 0,645 Z" fill="var(--swoosh)"/>
      <path d="M0,600 C200,700 500,600 790,685" fill="none" stroke="var(--swoosh-light)" stroke-width="8"/>
      <path d="M0,625 C240,700 540,605 780,685 L0,685 Z" fill="var(--swoosh)"/>
    </svg>

    <section class="certification">
      <span class="certification-mark"></span>
      <span class="certification-name">Corvane Standards Group</span>
      <div class="certification-rule"></div>
      <div class="certification-level">QUVEX® 7 Certified</div>
    </section>

    <header class="holder">
      <h1 class="holder-name">Dr Leopold Marsh</h1>
      <div class="holder-rule"></div>
      <div class="holder-credentials">PhD . QPL . FSBD</div>
    </header>

    <ul class="contact-list">
      <li class="contact-item">
        <svg class="contact-icon" viewBox="0 0 40 40" aria-hidden="true"><path d="M20 5 L37 20 H32 V35 H24 V25 H16 V35 H8 V20 H3 Z" fill="var(--ink)"/></svg>
        418 Kelvendale NSW 2093 Australia
      </li>
      <li class="contact-item">
        <svg class="contact-icon" viewBox="0 0 40 40" aria-hidden="true"><rect x="4" y="9" width="32" height="22" fill="none" stroke="var(--ink)" stroke-width="2.5"/><path d="M4 9 L20 22 L36 9 M4 31 L16 19 M36 31 L24 19" fill="none" stroke="var(--ink)" stroke-width="2.5"/></svg>
        leopold.marsh@lumora-pathway.org
      </li>
      <li class="contact-item">
        <svg class="contact-icon" viewBox="0 0 40 40" aria-hidden="true"><g fill="none" stroke="var(--ink)" stroke-width="2.2"><circle cx="20" cy="20" r="13"/><ellipse cx="20" cy="20" rx="6" ry="13"/><path d="M7 20 H33 M9 13 H31 M9 27 H31"/></g></svg>
        www.lumora-pathway.org
      </li>
      <li class="contact-item">
        <svg class="contact-icon" viewBox="0 0 40 40" aria-hidden="true"><ellipse cx="20" cy="20" rx="16" ry="14" fill="none" stroke="var(--ink)" stroke-width="2.5"/><path d="M14 11 L18 15 L16 18 C17 21 19 23 22 24 L25 22 L29 26 L26 29 C18 29 11 22 11 14 Z" fill="var(--ink)"/></svg>
        61 437 918000
      </li>
      <li class="contact-item is-continued">612 9368 2000</li>
    </ul>

    <div class="partner-badge" role="img" aria-label="KT Summit Associate partner badge"></div>
  </main>
</body>
</html>
```